Brochure for dynamic theatrical production company

New brochure for Heron Stageworks, featuring our current theatrical projects. We are a theatrical producing and consulting company, and we need the brochure to communicate the breadth of our projects. Our work is produced and performed throughtout the United States and also tours to Europe, Asia, the Middle East and South America. We also work with companies and artists from around the globe and bring them to the United States to tour and develop new work. Projects range from experimental multi-disciplinary works to Broadway musicals.

The brochure is meant to introduce other performing arts professionals to our work. These potential clients might engage one of our artists or projects for a performance, or they may engage us as consultants on additional projects.

The final design should be a standard size document that is fairly simple and inexpensive to reproduce. This is a piece that is used within the entertainment industry to develop interest in our work from other theaters, presenters, festivals, donors and artists.

I have included the pdf of last year's design, as well as a word document with the text to be used for this year. The world document also contains a link to a dropbox folder with photos and other supplementary materials as well.

You can also refer to our website for insights into our work and our aesthetic. www.heronstageworks-example.com

Target Market(s)

Industry professionals, funders/investors, prospective clients.

Industry/Entity Type

Entertainment Industry

Font styles to use
Sans Serif

Colors

Designer to choose colors to be used in the design.

Requirements
Must have
• Please use text provided in "Heron Brochure 2018" document. A variety of photos and other graphics are available for download via a link embedded in the document.
• Please make sure the finished piece can be printed on standard paper sizes in the US: For example: ledger size is 279 x 432 mm (11.0 x 17.0 in), letter size is 216 x 279 mm (8.5 x 11.0 in), Legal size is 216 x 356 mm (8.5 x 14.0 in)
Nice to have
• Our previous brochure and current website use pictures in the shape of circles (see sample attached). I would like that to be consistent with the new brochure. Website, for your reference, is www.heronstageworks-example.com
Should not have
• non-standard paper sizes

```html
<!DOCTYPE html>
<html lang="en">
<head>
<meta charset="utf-8">
<title>Heron Stageworks — Iphigenia</title>
<link rel="stylesheet" href="https://fonts.googleapis.com/css2?family=Didact+Gothic&family=Josefin+Sans:wght@700&family=Oswald:wght@600&family=Tinos:ital@1&display=swap">
<style>
  :root{
    --teal:#0a9faa;
    --teal-text:#1a9ea8;
    --cloud:#dfdbdb;
    --cloud-line:#cfcaca;
    --ink:#1b1b1b;
    --white:#ffffff;
  }
  html,body{margin:0;padding:0;width:1200px;height:988px;overflow:hidden;background:var(--white);}
  .canvas{width:1200px;height:988px;overflow:hidden;position:relative;}
  .page{width:1360px;height:1120px;position:absolute;left:0;top:0;transform:scale(0.88235);transform-origin:0 0;
    font-family:"Didact Gothic",sans-serif;color:var(--ink);}
  .shapes{position:absolute;left:0;top:0;}
  .abs{position:absolute;}
  .page-number{left:1320px;top:22px;font-size:13px;font-weight:bold;}
  .section-title{left:60px;top:170px;margin:0;font-family:"Josefin Sans",sans-serif;font-weight:700;font-size:38px;color:var(--teal-text);letter-spacing:1px;}
  .body-col{font-size:11.2px;line-height:16px;margin:0;}
  .body-col p{margin:0 0 16px;}
  .body-col b{font-weight:bold;}
  .about-1{left:47px;top:358px;width:185px;}
  .about-2{left:243px;top:358px;width:184px;}
  .about-3{left:440px;top:636px;width:182px;}
  .title-block{right:42px;top:64px;text-align:right;}
  .title-block .artists{font-size:15px;line-height:17px;}
  .title-block h1{margin:6px 0 4px;font-family:"Oswald",sans-serif;font-weight:600;font-size:42px;line-height:46px;letter-spacing:1px;}
  .title-block .dates{font-size:12.5px;line-height:15px;font-weight:bold;}
  .title-block .credits{margin-top:7px;font-size:12.5px;line-height:17.5px;font-style:italic;}
  .teal-col{color:var(--white);font-size:10.6px;line-height:14.7px;margin:0;}
  .teal-col p{margin:0 0 14.7px;}
  .teal-1{left:721px;top:332px;width:190px;}
  .teal-2{left:932px;top:332px;width:190px;}
  .teal-3{left:1143px;top:332px;width:180px;}
  .quote{left:1140px;top:576px;width:184px;text-align:right;color:var(--white);font-family:"Tinos",serif;font-style:italic;font-size:15px;line-height:19.5px;margin:0;}
  .quote cite{display:block;margin-top:16px;font-style:italic;}
  .artists-heading{left:680px;top:618px;width:230px;height:34px;margin:0;background:var(--ink);color:var(--white);
    font-family:"Didact Gothic",sans-serif;font-weight:normal;font-size:20px;line-height:36px;letter-spacing:.5px;text-indent:41px;}
  .bio{font-size:10.5px;line-height:14.7px;margin:0;}
  .bio-1{left:721px;top:663px;width:192px;}
  .bio-2{left:932px;top:663px;width:188px;}
  .partners-label{left:721px;top:1021px;margin:0;font-size:12.5px;color:var(--teal-text);}
  .partners{left:721px;top:1044px;display:flex;gap:18px;align-items:center;margin:0;padding:0;list-style:none;}
  .partner{font-size:11px;line-height:13px;color:var(--ink);max-width:96px;}
</style>
</head>
<body>
<div class="canvas">
<div class="page">

  <svg class="shapes" width="1360" height="1120" viewBox="0 0 1360 1120" aria-hidden="false">
    <defs>
      <radialGradient id="portraitTone" cx="50%" cy="55%" r="60%">
        <stop offset="0%" stop-color="#c69a7c"/>
        <stop offset="45%" stop-color="#8a5f44"/>
        <stop offset="100%" stop-color="#2c1d15"/>
      </radialGradient>
      <linearGradient id="scoreTone" x1="0" y1="0" x2="1" y2="1">
        <stop offset="0%" stop-color="#e4e2df"/>
        <stop offset="100%" stop-color="#a9a7a3"/>
      </linearGradient>
    </defs>

    <!-- grey cloud behind company text -->
    <g fill="var(--cloud)">
      <circle cx="130" cy="470" r="172"/>
      <circle cx="330" cy="445" r="205"/>
      <circle cx="330" cy="640" r="150"/>
      <circle cx="540" cy="735" r="130"/>
      <circle cx="545" cy="935" r="145"/>
      <circle cx="1292" cy="108" r="140"/>
    </g>
    <g fill="none" stroke="var(--cloud-line)" stroke-width="1.5">
      <circle cx="395" cy="710" r="268"/>
      <circle cx="300" cy="575" r="318"/>
    </g>

    <!-- teal cloud behind production text -->
    <g fill="var(--teal)">
      <circle cx="738" cy="412" r="135"/>
      <circle cx="930" cy="420" r="150"/>
      <circle cx="890" cy="515" r="90"/>
      <circle cx="1075" cy="430" r="150"/>
      <circle cx="1235" cy="405" r="135"/>
      <circle cx="1310" cy="440" r="90"/>
      <circle cx="1240" cy="622" r="120"/>
    </g>

    <circle cx="740" cy="120" r="136" fill="url(#portraitTone)" role="img" aria-label="Portrait photograph of the librettist"/>
    <circle cx="1292" cy="962" r="182" fill="url(#scoreTone)" role="img" aria-label="Photograph of the handwritten opera score"/>
  </svg>

  <div class="abs page-number">1</div>

  <h2 class="abs section-title">ABOUT</h2>

  <div class="abs body-col about-1">
    <p>Heron Stageworks was founded by creative producer Mira Isley and is dedicated to producing and consulting in the performing arts. From experimental to commercial, we collaborate with artists and organizations to foster an expansive range of compelling theatrical works for local, national and international audiences. We eschew boundaries—aesthetic,</p>
  </div>

  <div class="abs body-col about-2">
    <p>geopolitical, institutional—and thrive on a nimble and rigorous practice.<br>As <b>producers</b> we generate and develop our own innovative theatrical projects, serve as executive and creative producers for hire (by producing companies, independent artists and others) and provide other creative project-based services, including tour producing, program development and dramaturgy.</p>
    <p>As <b>consultants</b> we work with theater companies, presenters, performing arts centers, foundations and other non-profit or commercial entities to provide ongoing programming advice, research and development as well as broad policy, leadership and structural input and oversight.</p>
    <p>Our model of producing and consulting varies project-by-</p>
  </div>

  <div class="abs body-col about-3">
    <p>project, organization-by-organization. Our projects and clients reflect a broad spectrum of genre and scale. We examine the individual elements and/ or artists involved and shape producing strategy around their particular visions. By customizing an approach that capitalizes on the strengths of everyone involved and then identifying how to supplement those strengths we facilitate artistic excellence, while having a good time.</p>
    <p>At its core, Heron Stageworks combines artistic values with an independent flexibility and financial structure that allow us to create a body of work that wouldn't exist under any other auspice.</p>
  </div>

  <header class="abs title-block">
    <div class="artists">Warren Shelby<br>&amp; Estrella Sandoval</div>
    <h1>IPHIGENIA</h1>
    <div class="dates">Anticipated premiere Fall 2019<br>Available for touring 2019-2020</div>
    <div class="credits">Warren Shelby, Composer<br>Estrella Sandoval, Librettist<br>Opera Harborton, Co-Producer</div>
  </header>

  <div class="abs teal-col teal-1">
    <p>Warren Shelby and Estrella Sandoval's Iphigenia places the traditional operatic form in an improvisational environment. The evening length work is scored for chamber orchestra, Shelby's quartet and an ensemble of operatic and non-operatic vocalists.</p>
    <p>Aspects of Eurytides' original plays Iphigenia in Aulis and Iphigenia in Tauris serve as the basis for a reimagined libretto being written by</p>
  </div>
  <div class="abs teal-col teal-2">
    <p>Estrella Sandoval that scrutinizes the societal roles of women and men, reevaluating Eurytides' original plays and extending Iphigenia's transformative journey far beyond the scope of those works to challenge ancient narratives of religious war, female sacrifice, patriarchal politics, and the inevitability of choice being reduced to a lesser of two evils. The new libretto culminates in Iphigenia's return to Aulis, ushering in an awakening – in both genders–</p>
  </div>
  <div class="abs teal-col teal-3">
    <p>of feminine power, liberated from patriarchal imprisonment.</p>
    <p>Through the use of compositional and performance techniques that he has developed over the past two decades to create improvisational structures within symphonic compositions, Shelby's music will at times function as an "unspoken libretto", repurposing improvisation as a motivic narrative device.</p>
  </div>

  <blockquote class="abs quote">"Mr. Shelby's mastery is in knocking down the wall between jazz and classical."<cite>-Northgate Times</cite></blockquote>

  <h2 class="abs artists-heading">ABOUT THE ARTISTS</h2>

  <p class="abs bio bio-1">Considered by the Northgate Times as "Generally acknowledged to be jazz's greatest living composer", <b>Warren Shelby</b> has left an indelible mark on the development of music for the last half-century. He first rose to prominence in the late 1950's as the primary composer for Arlo Blakemore's Night Couriers. He next joined the Milo Davenport Quintet becoming what that bandleader referred to as the ensemble's "intellectual musical catalyst" before co-founding the pioneering group Cloud Bulletin. Since 2001, he has led his own highly acclaimed quartet. His works have been performed by the Lakeport Symphony, Riverbend Symphony, Valmont Symphony, National Coastal Radio Symphonic Orchestra, Lyrebird Chamber Orchestra, Eastbrook Philharmonic and Royal Hallstead Orchestra. In all, Mr. Shelby has realized over 200 compositions and dozens of these works have become modern standards.</p>

  <p class="abs bio bio-2">Bassist/composer/vocalist <b>Estrella Sandoval</b> combines influences and moves between musical worlds, performing and collaborating with the likes of Ruben Vale, Tomas Arriaga, Jack Delmont, Guido Reis, Greg Dunham, Janelle Morrow, Harvey Hale, Prentice, Sterling Wade, and Warren Shelby. Sandoval collaborated with Gil Garrison for her 2011 Chamber Song Society, breaking musical lines of jazz improvisation to classical music. This garnered her Best New Artist at the 53rd Golden Disc Awards, an unprecedented achievement by a jazz musician. The subsequently released Radio Song Society brought pop music together with a mosaic array of jazz legends and musicians. Both albums have led international music charts and gained multiple awards and Golden Discs.</p>

  <p class="abs partners-label">Commissioning partners:</p>
  <ul class="abs partners">
    <li class="partner">Capitol Arts Center</li>
    <li class="partner">Bayside Performances</li>
    <li class="partner">Arts Meridian</li>
    <li class="partner">Westvale Center for Performance</li>
  </ul>

</div>
</div>
</body>
</html>
```